Home Renovation Business needs a logo and business card design

I need a logo design for my home renovation company. I work hard to provide quality work for a fair price. I want a clean design that has something to make it pop and catch the eye. It should have somewhat of a modern feel to it. You can check out my website at www.kbbuildworks.com to see some examples of the type of work I do.
Updates

Hi Everyone,

For some reason, not all my information was posted. I would like the following contact information included in the design:

Phone: 365.417.9826        Email: kdrosmol@maplepost.ca        Website: www.kbbuildworks.com

Also, if you would like to include a list of the services I offer, then I'd like the card to be double sided. I provide the following services: Full kitchen, basement and bathroom renovations. Tile, laminate and hardwood installation. Decks, fences and sheds. Windows and doors.

Industry/Entity Type

Business

Requirements
Must have
• I want the following information listed on the card:
• KD Buildworks
• Kyle Drosmolen
• 365.417.9826
• kdrosmol@maplepost.ca
• www.kbbuildworks.com
Nice to have
• If you want you could also include the list of services I provide. If you include this list feel free to make the card double sided.
• Kitchen, bathroom and basement renovations
• Flooring installation
• Decks, fences and sheds
• Windows and doors
• I am not 100% sure if I want to include this on the card or not.

```html
<!DOCTYPE html>
<html lang="en">
<head>
<meta charset="utf-8">
<title>KD Buildworks – Business Card</title>
<link href="https://fonts.googleapis.com/css2?family=Jost:wght@400;500;600&family=Marcellus&display=swap" rel="stylesheet">
<style>
  :root {
    --backdrop: #8d8d8d;
    --card-dark: #1f1f1f;
    --card-light: #f4f4f2;
    --ink-light: #ffffff;
    --ink-muted: #d6d6d6;
    --ink-dark: #141414;
    --accent: #d9262b;
  }
  * { margin: 0; padding: 0; box-sizing: border-box; }
  html, body {
    width: 1200px; height: 1000px; overflow: hidden;
    background: var(--backdrop);
  }
  .stage { position: relative; width: 1200px; height: 1000px; }

  .card {
    position: absolute;
    width: 700px; height: 400px;
    border-radius: 4px;
    box-shadow: 0 10px 28px rgba(0,0,0,0.28);
  }

  /* Front */
  .card-front {
    left: 120px; top: 80px;
    background: var(--card-dark);
    color: var(--ink-light);
    font-family: "Jost", sans-serif;
  }
  .brand {
    position: absolute; left: 270px; top: 150px;
    display: flex; align-items: center; gap: 16px;
  }
  .brand-square {
    width: 34px; height: 34px; background: var(--accent);
  }
  .brand-name {
    font-family: "Jost", sans-serif;
    font-weight: 600; font-size: 34px;
    letter-spacing: 4px; text-transform: uppercase;
    color: var(--ink-light);
    white-space: nowrap;
  }
  .owner-name {
    position: absolute; left: 44px; top: 218px;
    font-size: 18px; font-weight: 500;
    letter-spacing: 1px; color: var(--ink-light);
  }
  .contact-list {
    position: absolute; left: 44px; top: 258px;
    list-style: none;
  }
  .contact-list li {
    display: flex; align-items: center; gap: 12px;
    font-size: 15px; color: var(--ink-muted);
    margin-bottom: 12px; letter-spacing: 0.5px;
  }
  .contact-icon {
    width: 18px; height: 18px; flex: none;
  }

  /* Back */
  .card-back {
    left: 380px; top: 520px;
    background: var(--card-light);
    color: var(--ink-dark);
    font-family: "Jost", sans-serif;
    text-align: center;
  }
  .services-title {
    font-family: "Marcellus", serif;
    font-weight: 400; font-size: 40px;
    letter-spacing: 9px;
    margin-top: 78px;
  }
  .services-list {
    list-style: none; margin-top: 18px;
    font-size: 16px; line-height: 1.45;
  }
  .site-line {
    position: absolute; right: 44px; bottom: 34px;
    font-size: 16px;
  }
</style>
</head>
<body>
<main class="stage">

  <section class="card card-front" aria-label="Card front">
    <div class="brand">
      <span class="brand-square"></span>
      <span class="brand-name">KD Buildworks</span>
    </div>
    <p class="owner-name">Kyle Drosmolen</p>
    <ul class="contact-list">
      <li>
        <svg class="contact-icon" viewBox="0 0 18 18" aria-hidden="true">
          <rect width="18" height="18" rx="3" fill="#ffffff"/>
          <path d="M5 4h3l1 3-1.5 1a7 7 0 0 0 2.5 2.5L11 9l3 1v3a1 1 0 0 1-1 1A9 9 0 0 1 4 5a1 1 0 0 1 1-1z" fill="#1f1f1f"/>
        </svg>
        <span>365.417.9826</span>
      </li>
      <li>
        <svg class="contact-icon" viewBox="0 0 18 18" aria-hidden="true">
          <rect width="18" height="18" rx="3" fill="#ffffff"/>
          <rect x="3.5" y="5" width="11" height="8" fill="none" stroke="#1f1f1f" stroke-width="1.4"/>
          <path d="M3.5 5l5.5 4.5L14.5 5" fill="none" stroke="#1f1f1f" stroke-width="1.4"/>
        </svg>
        <span>kdrosmol@maplepost.ca</span>
      </li>
      <li>
        <svg class="contact-icon" viewBox="0 0 18 18" aria-hidden="true">
          <rect width="18" height="18" rx="3" fill="#ffffff"/>
          <circle cx="9" cy="9" r="5" fill="none" stroke="#1f1f1f" stroke-width="1.3"/>
          <path d="M4 9h10M9 4c-2.5 3-2.5 7 0 10M9 4c2.5 3 2.5 7 0 10" fill="none" stroke="#1f1f1f" stroke-width="1.1"/>
        </svg>
        <span>www.kbbuildworks.com</span>
      </li>
    </ul>
  </section>

  <section class="card card-back" aria-label="Card back">
    <h2 class="services-title">OUR SERVICES</h2>
    <ul class="services-list">
      <li>Build a Full Kitchen, Basement And Bathroom Renovations</li>
      <li>Decking Fences and Sheds</li>
      <li>Tile, Laminate and Hardwood Installation</li>
      <li>Windows and Doors</li>
    </ul>
    <p class="site-line">Visit our web site :- www.kbbuildworks.com</p>
  </section>

</main>
</body>
</html>
```